Dr Mira Thalen, Orthopaedic Hand Surgeon

I am an orthopaedic hand surgeon and need business cards that reflect the surgery I do. I operate on bones, ligaments, tendons, and soft tissues. I can do microsurgery (surgery under an operating microscope) - including connecting ends of cut nerves and arteries in the fingers together. As an orthopaedic surgeon, I also fix fractures and manage orthopaedic trauma in the rest of the body. I favour black as a colour, and have some pictures of hand X-rays that you can use in the design, if you think that would look good (feel free to crop).
Updates

Hi all. Thank you for all your submissions so far. Please note that I have updated my project brief. I would like to emphasise that use of the logos that I have provided is optional, and if used, I would very much prefer the logo not to dominate the card, but add to the overall aesthetic of the card. Warm regards, Mira

Target Market(s)

Referring medical practitioners, hand therapists, patients

Industry/Entity Type

Healthcare

Contact Information for Business Card

Dr Mira Thalen
Orthopaedic Hand Surgeon
MBBS BSc (Med), MIntPH (Merit), FCWES (Ortho), FUPelV

Font styles to use
Serif

Colors

Designer to choose colors to be used in the design.

Requirements
Must have
• Space for:
• 2 addresses (a PO Box Address and a consulting suite address) - to be confirmed
• 1 phone number - to be confirmed
Nice to have
• Please choose one of the FCWES logos (I included 3 - colour, black reverse, and greyscale); if you include this in the design, IT SHOULD NOT DOMINATE THE CARD, but be smaller and more discreet.
• I have also attached the FUPelV logo (colour and greyscale); if you choose to include this in the design, IT SHOULD NOT DOMINATE THE CARD, but be smaller and more discreet.
• I would love to be able to update details on the card as time goes on, and thus would like to own the template for the card as well.
• Also I would love discussion with regard to any changes on the card, if I am not completely happy with the design, and would like to discuss things such as ease of printing, finish on the cards (matte, polish) etc.
Should not have
• I don't like the card to look too crowded

```html
<!DOCTYPE html>
<html lang="en">
<head>
<meta charset="utf-8">
<title>Dr Mira Thalen – Business Card</title>
<link href="https://fonts.googleapis.com/css2?family=Mulish:wght@400;600;800&display=swap" rel="stylesheet">
<style>
  :root {
    --backdrop: #e9e9e9;
    --card: #fbfcfc;
    --accent: #2a9fd8;
    --ink: #8a8a8a;
    --ink-soft: #b4b4b4;
    --mark: #9a9a9a;
  }
  * { box-sizing: border-box; margin: 0; padding: 0; }
  html, body { width: 1200px; height: 1200px; overflow: hidden; }
  body {
    background: var(--backdrop);
    font-family: "Mulish", Arial, sans-serif;
    display: flex; align-items: center; justify-content: center;
  }
  .business-card {
    position: relative;
    width: 1000px; height: 571px;
    background: var(--card);
    box-shadow: 0 6px 24px rgba(0,0,0,0.08);
  }
  .affiliations {
    position: absolute; top: 58px; left: 0; right: 0;
    display: flex; justify-content: center; gap: 26px;
  }
  .affiliation {
    display: flex; align-items: center; gap: 6px;
    font-size: 13px; font-weight: 600; color: var(--mark); letter-spacing: 0.5px;
  }
  .affiliation .seal {
    width: 20px; height: 20px; border-radius: 50%;
    border: 1.5px solid var(--mark);
  }
  .identity {
    position: absolute; top: 150px; left: 0; right: 0; text-align: center;
  }
  .identity .name {
    font-size: 40px; font-weight: 800; color: var(--accent); letter-spacing: 0.3px;
  }
  .identity .role {
    margin-top: 6px; font-size: 21px; color: var(--ink);
  }
  .identity .credentials {
    margin-top: 8px; font-size: 12px; color: var(--ink-soft);
  }
  .consulting {
    position: absolute; top: 300px; left: 700px;
    font-size: 16px; line-height: 1.4; color: var(--ink);
  }
  .consulting .heading {
    font-weight: 800; font-size: 18px; color: var(--accent);
  }
  .contact {
    position: absolute; left: 64px; bottom: 58px;
    font-size: 18px; line-height: 1.35; color: var(--ink);
  }
  .contact dt {
    display: inline-block; width: 30px; color: var(--accent); font-weight: 600;
  }
  .contact dd { display: inline; }
</style>
</head>
<body>
  <article class="business-card">
    <div class="affiliations">
      <span class="affiliation"><span class="seal"></span>FUPelV</span>
      <span class="affiliation"><span class="seal"></span>FCWES</span>
    </div>

    <header class="identity">
      <h1 class="name">Dr. Mira Thalen</h1>
      <p class="role">Orthopaedic Hand Surgeon</p>
      <p class="credentials">MBBS BSc (Med), MIntPH (Merit), FCWES (Ortho), FUPelV</p>
    </header>

    <address class="consulting">
      <div class="heading">Consulting Address</div>
      <div>Larkmoor Lane No. 18</div>
      <div>PO BOX 40716 - Eastvale</div>
    </address>

    <dl class="contact">
      <div><dt>T :</dt><dd>+61 2 5550 1482</dd></div>
      <div><dt>M :</dt><dd>+61 455 019 376</dd></div>
      <div><dt>E :</dt><dd>mira.thalen@handclinic.example</dd></div>
    </dl>
  </article>
</body>
</html>
```